Veltarum

Standard Business Card design.
Sample two-sided design uploaded. White front, Black back.
Would like white shield to be on all black background side.
Willing to look at a couple creative designs, but nothing crazy.
Preference for a classic, confident, strong design.

```html
<!DOCTYPE html>
<html lang="en">
<head>
<meta charset="utf-8">
<title>Veltarum Business Card</title>
<link rel="stylesheet" href="https://fonts.googleapis.com/css2?family=Montserrat:wght@400;500;700&display=swap">
<style>
  :root {
    --canvas: #2a2a2c;
    --card: #1c1c1d;
    --card-edge: #262627;
    --gloss: #3b3b3d;
    --ink: #f2f2f2;
    --ink-soft: #c9c9c9;
  }
  * { box-sizing: border-box; margin: 0; padding: 0; }
  html, body { width: 1200px; height: 900px; overflow: hidden; }
  body {
    background: var(--canvas);
    font-family: "Montserrat", sans-serif;
    position: relative;
  }
  .card {
    position: absolute;
    width: 540px;
    height: 310px;
    background: var(--card);
    border: 1px solid var(--card-edge);
    border-radius: 16px;
    box-shadow: 0 18px 40px rgba(0,0,0,.45);
  }
  .card--front { left: 50px; top: 140px; }
  .card--back { left: 610px; top: 450px; }

  .brand {
    display: flex;
    align-items: center;
    gap: 12px;
    font-weight: 700;
    letter-spacing: .14em;
    text-transform: uppercase;
  }
  .brand__mark { display: block; }

  .card--front .brand {
    position: absolute;
    left: 50%; top: 50%;
    transform: translate(-50%, -50%);
    font-size: 40px;
    color: var(--gloss);
  }
  .card--front .brand__mark { width: 30px; height: 30px; background: var(--gloss); }

  .card--back .brand {
    position: absolute;
    left: 30px; top: 34px;
    font-size: 22px;
    color: var(--ink);
  }
  .card--back .brand__mark { width: 16px; height: 16px; background: var(--ink); }

  .address {
    position: absolute;
    right: 30px; top: 34px;
    text-align: right;
    font-size: 12px;
    line-height: 1.5;
    color: var(--ink-soft);
  }

  .person { position: absolute; left: 30px; top: 128px; }
  .person__name { font-size: 22px; font-weight: 700; color: var(--ink); }
  .person__title { font-size: 13px; color: var(--ink-soft); margin-top: 2px; }

  .contacts {
    position: absolute;
    left: 30px; bottom: 26px;
    list-style: none;
    font-size: 12px;
    color: var(--ink);
  }
  .contacts li { display: flex; align-items: center; gap: 10px; height: 20px; }
  .contacts svg { width: 12px; height: 12px; fill: none; stroke: var(--ink); stroke-width: 1.6; }
</style>
</head>
<body>
  <section class="card card--front" aria-label="Card front">
    <div class="brand"><span class="brand__mark"></span>Veltarum</div>
  </section>

  <section class="card card--back" aria-label="Card back">
    <div class="brand"><span class="brand__mark"></span>Veltarum</div>

    <address class="address">418 Linden Park Ave, #112<br>Corvell, OH 43190</address>

    <div class="person">
      <p class="person__name">Daren Holloway</p>
      <p class="person__title">Managing Director</p>
    </div>

    <ul class="contacts">
      <li><svg viewBox="0 0 12 12"><path d="M2 1.5h2.5l1 2.5-1.5 1a6 6 0 0 0 3 3l1-1.5 2.5 1V11A9 9 0 0 1 1 2z"/></svg>877-555-0142</li>
      <li><svg viewBox="0 0 12 12"><rect x="3" y="1" width="6" height="10" rx="1"/><path d="M5.5 9.2h1"/></svg>877-555-0142</li>
      <li><svg viewBox="0 0 12 12"><rect x="1" y="2.5" width="10" height="7"/><path d="M1 2.5l5 4 5-4"/></svg>info@veltarumgroup.com</li>
      <li><svg viewBox="0 0 12 12"><circle cx="6" cy="6" r="5"/><path d="M1 6h10M6 1c2 2.5 2 7.5 0 10M6 1c-2 2.5-2 7.5 0 10"/></svg>www.veltarumgroup.com</li>
    </ul>
  </section>
</body>
</html>
```